Web Site Redesign

We operate a data centre facility specialing in colocation and Fibre optic connectivity (i.e. point to point fibre services and internet over fibre).

We have an existing site located at www.norvalex.example however this is very very tired and requires a redesign. We are looking for a fresh new design that will be appealing to potential customers.

The Company name is Norva eX and the primary corporate colour is bright red with secondary colours of white, grey and black. Specific bright red can be seen in attached company logo.

Website needs to be modern, clean and professional representing our premium colocation and fibre provider branding.

Our company slogan is : safe. secure. reliable

We will provide feedback regardless of the quality of the design to ensure a better outcome for all parties.

Please feel free to contact us if you have any questions.

# The designer can use placeholder images or feel free to use any/all or none of the attached images
# The designer can use sample filler text

Target Market(s)

Technical IT Professionals as well C level executives (i.e. CEO's, CIO).

Industry/Entity Type

Internet

Requirements
Must have
• clean design
Nice to have
• A sidebar with two sections. 1 for current promo and 1 for "Let us call you back/contact you"
Should not have
• Clutter

```html
<!DOCTYPE html>
<html lang="en">
<head>
<meta charset="utf-8">
<title>Norva eX Client WebMail</title>
<link rel="stylesheet" href="https://fonts.googleapis.com/css2?family=Arimo:ital,wght@0,400;0,700;1,400&display=swap">
<style>
  :root {
    --red: #cc3333;
    --black: #000000;
    --ink: #111111;
    --page: #f2eeed;
    --panel: #ffffff;
    --panel-soft: #f9f8f8;
    --line: #dedada;
    --field: #e2e2e2;
  }
  * { box-sizing: border-box; margin: 0; padding: 0; }
  html, body { width: 1200px; height: 657px; overflow: hidden; }
  body {
    position: relative;
    background: var(--page);
    font-family: "Arimo", Arial, sans-serif;
    color: var(--ink);
  }
  .abs { position: absolute; }

  /* Header */
  .brand {
    left: 118px; top: 96px;
    display: flex; align-items: center; gap: 8px;
    font-size: 20px; color: var(--black);
    text-transform: uppercase; letter-spacing: 1px;
  }
  .brand-mark { width: 18px; height: 18px; background: var(--red); flex: none; }
  .tagline { left: 263px; top: 22px; width: 324px; }
  .tagline .city { font-size: 14px; }
  .tagline .slogan { font-size: 30px; font-style: italic; letter-spacing: -0.4px; line-height: 32px; white-space: nowrap; }
  .tagline .sub { font-size: 13px; text-align: right; }
  .contact-lines { right: 118px; top: 31px; text-align: right; font-size: 12px; line-height: 20px; }
  .contact-lines span { display: flex; align-items: center; justify-content: flex-end; gap: 7px; }

  /* Navigation */
  .main-nav {
    left: 261px; top: 100px; width: 823px; height: 37px;
    background: var(--red); display: flex;
  }
  .main-nav a {
    color: #fff; text-decoration: none; font-size: 14px; white-space: nowrap;
    display: flex; align-items: center; justify-content: center; height: 100%;
  }
  .main-nav a.active { background: var(--black); }

  /* Banner */
  .banner { left: 103px; top: 141px; width: 982px; height: 100px; background: var(--red); }
  .banner h1 { position: absolute; left: 25px; top: 33px; color: #fff; font-size: 30px; font-weight: 400; font-style: italic; }
  .banner-photo {
    position: absolute; right: 0; top: 0; width: 260px; height: 100px;
    background: linear-gradient(90deg, rgba(204,51,51,1) 0%, #c9c9cc 45%, #8b8d92 100%);
  }

  /* Breadcrumb */
  .crumbs {
    left: 103px; top: 249px; width: 981px; height: 27px;
    background: var(--panel); border: 1px solid var(--line);
    display: flex; align-items: center; justify-content: space-between;
    padding: 0 12px; font-size: 11px;
  }
  .crumbs .label { color: var(--red); }

  /* Content */
  .content { left: 103px; top: 287px; width: 758px; height: 267px; background: var(--panel); border: 1px solid var(--line); }
  .content h2 { position: absolute; left: 24px; top: 19px; font-size: 18px; font-weight: 400; color: var(--red); }
  .login-form { position: absolute; left: 24px; top: 72px; }
  .form-row { display: flex; align-items: center; height: 31px; }
  .form-row label { width: 131px; font-size: 12px; font-weight: 700; }
  .form-row .field { width: 180px; height: 27px; background: var(--field); border: 0; }
  .check-btn {
    margin: 0 0 0 131px; width: 180px; height: 26px; border: 0;
    background: var(--red); color: #fff; font: 12px "Arimo", Arial, sans-serif;
  }
  .notice { position: absolute; left: 24px; top: 205px; display: flex; font-size: 12px; line-height: 18px; }
  .notice strong { width: 131px; flex: none; }
  .notice p { width: 565px; hyphens: auto; -webkit-hyphens: auto; }

  /* Sidebar */
  .testimonials { left: 868px; top: 287px; width: 217px; height: 267px; background: var(--panel-soft); border: 1px solid var(--line); overflow: hidden; }
  .testimonials svg { position: absolute; left: -1px; top: -1px; }
  .quote { position: absolute; left: 43px; top: 53px; width: 162px; font-size: 12px; line-height: 16px; hyphens: auto; -webkit-hyphens: auto; }
  .quote-author { position: absolute; left: 44px; top: 225px; font-size: 11px; color: var(--red); }

  /* Footer */
  .footer-rule { left: 103px; top: 565px; width: 981px; height: 4px; background: var(--black); }
  .copyright { left: 104px; top: 584px; font-size: 11px; }
  .footer-links { left: 105px; top: 602px; font-size: 11px; color: var(--red); }
  .footer-links .sep { color: var(--ink); margin: 0 6px; }
  .footer-badges { left: 797px; top: 581px; display: flex; gap: 5px; }
  .footer-badges span { width: 68px; height: 20px; color: #fff; font-size: 11px; display: flex; align-items: center; justify-content: center; }
  .footer-badges .dark { background: var(--black); }
  .footer-badges .red { background: var(--red); }
</style>
</head>
<body>
  <header>
    <div class="abs brand"><span class="brand-mark"></span>Norva eX</div>
    <div class="abs tagline">
      <div class="city">Perth's</div>
      <div class="slogan">Save, Secure &amp; Reliable</div>
      <div class="sub">Data Centre</div>
    </div>
    <div class="abs contact-lines">
      <span>sales@norvalex.example
        <svg width="15" height="10" viewBox="0 0 15 10"><rect width="15" height="10" fill="#cc3333"/><path d="M0 0 L7.5 6 L15 0" fill="none" stroke="#fff" stroke-width="1.2"/></svg></span>
      <span>+1 555 010 2040
        <svg width="15" height="10" viewBox="0 0 15 10"><path d="M1 4 Q7.5 -1 14 4 L12 5 L10 3 L5 3 L3 5 Z" fill="#cc3333"/><rect x="3" y="5" width="9" height="5" fill="#cc3333"/></svg></span>
    </div>
    <nav class="abs main-nav">
      <a href="#" style="width:79px">Home</a>
      <a href="#" style="width:100px">About Us</a>
      <a href="#" style="width:100px">Facilities&nbsp;▾</a>
      <a href="#" style="width:144px">Business Continuity</a>
      <a href="#" style="width:106px">Services▾</a>
      <a href="#" style="width:95px">Partners</a>
      <a href="#" class="active" style="width:96px">Webmail</a>
      <a href="#" style="width:103px">Contact Us</a>
    </nav>
  </header>

  <section class="abs banner">
    <h1>Norva eX Client WebMail</h1>
    <div class="banner-photo" role="img" aria-label="Close-up photograph of computer keyboard keys"></div>
  </section>

  <div class="abs crumbs">
    <div><span class="label">You're Here :</span>&nbsp; Home :: Web Mail</div>
    <div>Monday, August 16 2010</div>
  </div>

  <main class="abs content">
    <h2>Norva eX Client WebMail</h2>
    <form class="login-form">
      <div class="form-row"><label>Account Name</label><input class="field" type="text"></div>
      <div class="form-row"><label>Account Password</label><input class="field" type="password"></div>
      <div class="form-row"><label>POP3 Server</label><input class="field" type="text"></div>
      <button class="check-btn" type="button">Check Mail Now</button>
    </form>
    <div class="notice">
      <strong>Trespasser Notice:</strong>
      <p>By accessing this service, you confirm you are an authorised user and have agreed to the Terms &amp; Conditions of Use. Unauthorised use may be referred to the appropriate authorities.</p>
    </div>
  </main>

  <aside class="abs testimonials">
    <svg width="100" height="86" viewBox="0 0 100 86">
      <polygon points="68,0 98,0 0,86 0,56" fill="#000"/>
      <text x="0" y="0" transform="translate(10,62) rotate(-41)" fill="#fff" font-family="Arimo, Arial, sans-serif" font-size="9">TESTIMONIALS</text>
    </svg>
    <p class="quote" lang="en">Lorem ipsum dolor sit amet, consectetuer adipiscing elit. Donec molestie. Sed aliquam sem ut arcu. Phasellus sollicitudin. Vestibulum condimentum facilisis nulla. In hac habitasse platea dictumst. Nulla nonummy. Cras quis libero.<br>Cras venenatis ....</p>
    <div class="quote-author">Jane Doe, example.com</div>
  </aside>

  <footer>
    <div class="abs footer-rule"></div>
    <div class="abs copyright">Copyright © 2010 by NorvaeX. All Right Reserved.</div>
    <div class="abs footer-links">Term Of Use<span class="sep">|</span>Privacy Policy<span class="sep">&nbsp;|&nbsp;</span>Contact Us</div>
    <div class="abs footer-badges">
      <span class="dark">Friendlink</span>
      <span class="dark">Chatline</span>
      <span class="red">XHTML</span>
      <span class="red">CSS</span>
    </div>
  </footer>
</body>
</html>
```